Business Card, letterhead, with compliment slip, envelope
Use same font as used in my logo
Use font as close as possible to what is in logo, unless it looks too heavy
Simple
Ned Calloway
412 Tarnwick Road Eynesbury 3338
ned@tarnwickfencing.com.au
http://www.tarnwickfencing.com.au
Use option 1 on the front of the card and option 2 of the logo on the back of the card. Keep to using white, orange and black. Do not go overboard with the fencing theme.
Option 2 of the logo.

```html
<!DOCTYPE html>
<html lang="en">
<head>
<meta charset="utf-8">
<title>Tarnwick Fencing Stationery</title>
<link rel="stylesheet" href="https://fonts.googleapis.com/css2?family=Open+Sans:wght@400;600;700&family=Oswald:wght@500;600&display=swap">
<style>
  :root {
    --paper: #ffffff;
    --ink: #1a1a1a;
    --grey: #555555;
    --orange: #f39a1e;
    --frame: #d9d9d9;
    --flap: #c8c8c8;
    --shadow: rgba(0, 0, 0, 0.22);
  }
  * { box-sizing: border-box; margin: 0; padding: 0; }
  html, body { width: 1200px; height: 933px; overflow: hidden; background: var(--paper); }
  body { position: relative; font-family: "Open Sans", Arial, sans-serif; color: var(--ink); }

  .board { position: absolute; left: 25px; top: 25px; width: 1155px; height: 881px; border: 1px solid var(--frame); }

  .sheet { position: absolute; background: var(--paper); box-shadow: 3px 4px 10px var(--shadow); }
  .slip { left: 64px; width: 434px; height: 212px; }
  .slip-plain { top: 107px; }
  .slip-compliments { top: 370px; }
  .envelope { left: 64px; top: 620px; width: 434px; height: 223px; overflow: hidden; }
  .letterhead { left: 613px; top: 153px; width: 332px; height: 626px; }
  .card { left: 975px; width: 141px; height: 82px; overflow: hidden; }
  .card-front { top: 230px; }
  .card-back { top: 357px; }

  .brand { position: absolute; display: flex; align-items: center; gap: 5px; }
  .brand-dot { flex: none; border-radius: 50%; background: var(--ink); }
  .brand-name { font-family: "Oswald", "Arial Narrow", sans-serif; font-weight: 600; color: var(--ink); text-transform: uppercase; letter-spacing: 0.04em; line-height: 1.05; }

  .slip .brand { left: 12px; top: 14px; }
  .slip .brand-dot { width: 38px; height: 38px; }
  .slip .brand-name { font-size: 12px; width: 64px; }

  .compliments-title { position: absolute; right: 20px; top: 26px; font-family: "Oswald", "Arial Narrow", sans-serif; font-weight: 500; font-size: 13px; letter-spacing: 0.04em; }

  .footer { position: absolute; left: 0; right: 0; text-align: center; font-size: 5.4px; line-height: 8px; color: var(--grey); white-space: nowrap; }
  .slip .footer { bottom: 22px; }
  .letterhead .footer { bottom: 24px; }
  .footer-rule { display: inline-flex; align-items: center; gap: 6px; }
  .rule { display: inline-block; width: 30px; height: 4px; }
  .footer strong { color: var(--ink); font-weight: 600; }

  .envelope-flap { position: absolute; left: 0; top: 0; }
  .envelope .brand { left: 50%; top: 30px; transform: translateX(-50%); }
  .envelope .brand-dot { width: 30px; height: 30px; }
  .envelope .brand-name { font-size: 10px; width: 56px; }

  .letterhead .brand { left: 50%; top: 22px; transform: translateX(-50%); }
  .letterhead .brand-dot { width: 36px; height: 36px; }
  .letterhead .brand-name { font-size: 11px; width: 60px; }

  .card-front .brand { left: 50%; top: 9px; transform: translateX(-50%); gap: 3px; }
  .card-front .brand-dot { width: 18px; height: 18px; }
  .card-front .brand-name { font-size: 5.5px; width: 30px; }
  .card-person { position: absolute; left: 12px; top: 37px; font-size: 4.6px; line-height: 6px; color: var(--grey); }
  .card-person .name { color: var(--orange); font-weight: 700; font-size: 5px; }
  .card-contact { position: absolute; left: 0; right: 0; bottom: 8px; text-align: center; font-size: 3.8px; line-height: 5px; color: var(--grey); white-space: nowrap; }

  .card-back .brand { left: 50%; top: 22px; transform: translateX(-50%); flex-direction: column; gap: 4px; }
  .card-back .brand-dot { width: 16px; height: 16px; }
  .card-back .brand-name { font-size: 9px; color: var(--orange); white-space: nowrap; }
</style>
</head>
<body>
  <div class="board"></div>

  <section class="sheet slip slip-plain">
    <div class="brand"><span class="brand-dot"></span><span class="brand-name">Tarnwick Fencing</span></div>
    <div class="footer">
      <div class="footer-rule"><svg class="rule" viewBox="0 0 30 4"><path d="M0 2H26M26 0L30 2L26 4Z" stroke="#f39a1e" fill="#f39a1e" stroke-width="1.2"/></svg><span><strong>412 Tarnwick Road</strong> | Harlow Vale 3391 | Call 0400 118 254</span><svg class="rule" viewBox="0 0 30 4"><path d="M30 2H4M4 0L0 2L4 4Z" stroke="#f39a1e" fill="#f39a1e" stroke-width="1.2"/></svg></div>
      <div>Fax 03 9100 4372 | ned@tarnwickfencing.com.au | www.tarnwickfencing.com.au</div>
    </div>
  </section>

  <section class="sheet slip slip-compliments">
    <div class="brand"><span class="brand-dot"></span><span class="brand-name">Tarnwick Fencing</span></div>
    <h2 class="compliments-title">WITH COMPLIMENTS</h2>
    <div class="footer">
      <div class="footer-rule"><svg class="rule" viewBox="0 0 30 4"><path d="M0 2H26M26 0L30 2L26 4Z" stroke="#f39a1e" fill="#f39a1e" stroke-width="1.2"/></svg><span><strong>412 Tarnwick Road</strong> | Harlow Vale 3391 | Call 0400 118 254</span><svg class="rule" viewBox="0 0 30 4"><path d="M30 2H4M4 0L0 2L4 4Z" stroke="#f39a1e" fill="#f39a1e" stroke-width="1.2"/></svg></div>
      <div>Fax 03 9100 4372 | ned@tarnwickfencing.com.au | www.tarnwickfencing.com.au</div>
    </div>
  </section>

  <section class="sheet envelope">
    <svg class="envelope-flap" width="434" height="90" viewBox="0 0 434 90"><path d="M0 0L200 78Q217 84 234 78L434 0" fill="none" stroke="#c8c8c8" stroke-width="1"/></svg>
    <div class="brand"><span class="brand-dot"></span><span class="brand-name">Tarnwick Fencing</span></div>
  </section>

  <section class="sheet letterhead">
    <div class="brand"><span class="brand-dot"></span><span class="brand-name">Tarnwick Fencing</span></div>
    <div class="footer">
      <div class="footer-rule"><svg class="rule" viewBox="0 0 30 4"><path d="M0 2H26M26 0L30 2L26 4Z" stroke="#f39a1e" fill="#f39a1e" stroke-width="1.2"/></svg><span><strong>412 Tarnwick Road</strong> | Harlow Vale 3391 | Call 0400 118 254</span><svg class="rule" viewBox="0 0 30 4"><path d="M30 2H4M4 0L0 2L4 4Z" stroke="#f39a1e" fill="#f39a1e" stroke-width="1.2"/></svg></div>
      <div>Fax 03 9100 4372 | ned@tarnwickfencing.com.au | www.tarnwickfencing.com.au</div>
    </div>
  </section>

  <section class="sheet card card-front">
    <div class="brand"><span class="brand-dot"></span><span class="brand-name">Tarnwick Fencing</span></div>
    <div class="card-person"><div class="name">Ned Calloway</div><div>Director</div></div>
    <div class="card-contact">
      <div>412 Tarnwick Road Harlow Vale 3391 | 0400 118 254</div>
      <div>ned@tarnwickfencing.com.au | www.tarnwickfencing.com.au</div>
    </div>
  </section>

  <section class="sheet card card-back">
    <div class="brand"><span class="brand-dot"></span><span class="brand-name">Tarnwick Fencing</span></div>
  </section>
</body>
</html>
```